Lumen Keyvault Password Manager WebApp Design

Lumen Keyvault is seeking an expert UI designer to provide a fresh and modern visual appeal for our product. Our inspiration comes from two major tools that have successfully managed to balance functionality and design aesthetics - Orbix Folder and Vaultmint. We want our application to exude a similar trustworthiness and modernity, through a clean, intuitive and responsive design.
We have established preliminary mockups and would like the designer to work within these parameters while enhancing the overall user experience. The primary tasks will involve innovative and improved designs of the login screen and the password screen, both being crucial touchpoints for our users. The login screen also serves a crucial role in demonstrating how our system works.
Key Elements:
Logo Integration: We are providing the logo for Lumen Keyvault. The design should align with the logo, both in terms of colors and overall aesthetic, to ensure a cohesive brand identity.
Color Palette: The UI design should adhere to the color palette derived from the logo to maintain brand consistency. The design should effectively utilize these colors to highlight important elements and improve user engagement.
Trustworthy and Modern Design: The UI should be professional and trustworthy. It should mirror the look and feel of Orbix Folder's simplicity and Vaultmint's solid security design, which inspires user confidence.
Adherence to Mockup Boundaries: The existing mockups serve as a guideline for the layout and placement of elements. The design should respect these boundaries while bringing innovation and visual appeal.
Improved Login Screen: The login screen is a key part of the user's journey and should be designed with utmost care. It should be intuitive, easy-to-use, visually engaging, and educative, showcasing how the system operates and encouraging users to sign in with confidence.
Enhanced Password Screen: The password screen, another key user touchpoint, needs improvement. The different types of passwords should be made more visible and intuitive, easing user interaction and enhancing the overall experience.
Prospective designers are encouraged to test our current version available for free at app.lumenkeyvault.com to understand the product better and contribute to meaningful design enhancements.
The goal of this project is to provide a visually compelling and user-friendly interface for Lumen Keyvault that inspires user trust, while adhering to the branding elements, including color scheme and logo design. The ideal designer will have a proven track record of creating compelling UI designs that enhance user experience and engagement.
We preferred the design to be in Figma.
Please provide the 3 design so we can evaluate if we like to choice you:
1. Login Page.
2. Passwords View design
3. Single Passwod Page
We need all the pages to be design that are provided as screenshots.

```html
<!DOCTYPE html>
<html lang="en">
<head>
<meta charset="utf-8">
<title>Lumen Keyvault — Vault</title>
<link href="https://fonts.googleapis.com/css2?family=Roboto:wght@400;500;700&display=swap" rel="stylesheet">
<style>
  :root {
    --sidebar: #2b313d;
    --sidebar-line: #3a414e;
    --sidebar-icon: #9aa1ad;
    --accent: #4a72c4;
    --page: #f0f1fb;
    --white: #ffffff;
    --item: #f8f8fc;
    --ink: #2a2e36;
    --text: #454a52;
    --muted: #6b7079;
    --line: #d9dbe3;
  }
  * { box-sizing: border-box; margin: 0; padding: 0; }
  html, body { width: 1200px; height: 800px; overflow: hidden; }
  body { font-family: "Roboto", sans-serif; background: var(--page); color: var(--text); position: relative; }

  .sidebar { position: absolute; left: 0; top: 0; width: 123px; height: 800px; background: var(--sidebar); }
  .brand { height: 83px; border-bottom: 1px solid var(--sidebar-line); display: flex; align-items: center; justify-content: center; gap: 5px; }
  .brand-mark { width: 9px; height: 9px; background: var(--white); border-radius: 2px; }
  .brand-name { color: var(--white); font-size: 11px; font-weight: 500; }
  .nav-vault { position: absolute; left: 38px; top: 150px; width: 54px; height: 53px; background: var(--accent); border-radius: 7px; color: var(--white); font-size: 10px; display: flex; flex-direction: column; align-items: center; justify-content: center; gap: 3px; }
  .nav-icon { position: absolute; left: 54px; width: 22px; height: 22px; }
  .side-foot { position: absolute; left: 25px; display: flex; align-items: center; gap: 10px; color: var(--sidebar-icon); font-size: 12px; }

  .header { position: absolute; left: 123px; top: 0; right: 0; height: 83px; background: var(--white); }
  .search { position: absolute; left: 36px; top: 17px; width: 302px; height: 43px; border: 1px solid #c9ccd4; border-radius: 8px; display: flex; align-items: center; padding-left: 15px; font-size: 12px; color: var(--muted); }
  .search-btn { position: absolute; right: 7px; top: 5px; width: 30px; height: 30px; background: var(--accent); border-radius: 6px; display: flex; align-items: center; justify-content: center; }
  .user { position: absolute; right: 54px; top: 21px; display: flex; align-items: center; gap: 11px; }
  .user-name { font-size: 13px; font-weight: 700; color: var(--ink); }
  .user-link { font-size: 12px; color: var(--muted); margin-top: 3px; display: flex; align-items: center; gap: 6px; }
  .avatar { width: 42px; height: 42px; border-radius: 50%; background: linear-gradient(135deg, #5a7fa6, #8a6a52); }

  .section-title { position: absolute; font-size: 20px; font-weight: 500; color: var(--ink); }
  .categories { position: absolute; left: 148px; top: 146px; width: 250px; height: 627px; background: var(--item); border-radius: 8px; overflow: hidden; }
  .category { height: 59px; border-bottom: 1px solid var(--white); display: flex; align-items: center; padding-left: 20px; gap: 12px; font-size: 15px; color: var(--text); position: relative; }
  .category svg { width: 18px; height: 18px; flex: none; }
  .category .chev { position: absolute; right: 20px; width: 12px; height: 12px; }

  .recent { position: absolute; left: 423px; top: 144px; width: 752px; height: 629px; background: var(--white); border-radius: 10px; }
  .recent-col { position: absolute; top: 24px; height: 400px; }
  .recent-col + .recent-col { border-left: 1px solid var(--line); }
  .entry { height: 60px; display: flex; align-items: flex-start; gap: 11px; padding-top: 11px; font-size: 15px; color: var(--text); }
  .entry svg { width: 18px; height: 17px; flex: none; }
</style>
</head>
<body>
  <aside class="sidebar">
    <div class="brand"><span class="brand-mark"></span><span class="brand-name">Lumen Keyvault</span></div>
    <div class="nav-vault">
      <svg width="22" height="20" viewBox="0 0 22 20" fill="none" stroke="#fff" stroke-width="2"><path d="M2 9 11 2l9 7v9H2z"/></svg>
      Vault
    </div>
    <svg class="nav-icon" style="top:237px" viewBox="0 0 22 22" fill="none" stroke="#9aa1ad" stroke-width="1.5"><circle cx="11" cy="6" r="2.5"/><circle cx="4.5" cy="9" r="2"/><circle cx="17.5" cy="9" r="2"/><path d="M6 20v-5a5 5 0 0 1 10 0v5M1.5 19v-3a3 3 0 0 1 3-3M20.5 19v-3a3 3 0 0 0-3-3"/></svg>
    <svg class="nav-icon" style="top:292px" viewBox="0 0 22 22" fill="none" stroke="#9aa1ad" stroke-width="1.5"><path d="M4 16V10a7 7 0 0 1 14 0v6zM2 16h18M9 19h4"/></svg>
    <svg class="nav-icon" style="top:347px" viewBox="0 0 22 22" fill="none" stroke="#9aa1ad" stroke-width="1.5"><path d="M3 4h16M3 11h12M3 18h16"/></svg>
    <div class="side-foot" style="top:718px">
      <svg width="16" height="16" viewBox="0 0 16 16" fill="none" stroke="#9aa1ad" stroke-width="1.3"><circle cx="8" cy="8" r="7"/><path d="M6 6.2a2 2 0 1 1 2.6 1.9c-.5.2-.6.5-.6 1v.4M8 11.5v.5"/></svg>Help
    </div>
    <div class="side-foot" style="top:749px">
      <svg width="16" height="16" viewBox="0 0 16 16" fill="none" stroke="#9aa1ad" stroke-width="1.3"><path d="M12 4.5A6.5 6.5 0 1 0 12 11.5M7 8h8M12.5 5.5 15 8l-2.5 2.5"/></svg>Log out
    </div>
  </aside>

  <header class="header">
    <div class="search">Search...
      <span class="search-btn"><svg width="15" height="15" viewBox="0 0 15 15" fill="none" stroke="#fff" stroke-width="1.5"><circle cx="6.5" cy="6.5" r="5"/><path d="m10.5 10.5 3 3"/></svg></span>
    </div>
    <div class="user">
      <div>
        <div class="user-name">Tharin Welikala</div>
        <div class="user-link">View profile <svg width="9" height="6" viewBox="0 0 9 6" fill="none" stroke="#6b7079" stroke-width="1.3"><path d="m1 1 3.5 3.5L8 1"/></svg></div>
      </div>
      <div class="avatar" role="img" aria-label="Profile photo of the signed-in user"></div>
    </div>
  </header>

  <h2 class="section-title" style="left:167px;top:108px">Categories</h2>
  <nav class="categories">
    <div class="category"><svg viewBox="0 0 18 18" fill="none" stroke="#454a52" stroke-width="1.3"><rect x="2" y="2" width="5" height="7"/><rect x="11" y="2" width="5" height="4"/><rect x="2" y="12" width="5" height="4"/><rect x="11" y="9" width="5" height="7"/></svg>General</div>
    <div class="category"><svg viewBox="0 0 18 18" fill="none" stroke="#454a52" stroke-width="1.3"><circle cx="8" cy="5" r="3.2"/><path d="M2 17v-1a6 6 0 0 1 8-5.6M12 14h5M15 12l2 2-2 2"/></svg>Shared with me</div>
    <div class="category"><svg viewBox="0 0 18 18" fill="none" stroke="#454a52" stroke-width="1.3"><rect x="1.5" y="5" width="15" height="11"/><path d="M6 5V2.5h6V5M1.5 10h15"/></svg>Work<svg class="chev" viewBox="0 0 12 12" fill="none" stroke="#454a52" stroke-width="1.3"><path d="m2 4 4 4 4-4"/></svg></div>
    <div class="category"><svg viewBox="0 0 18 18" fill="none" stroke="#454a52" stroke-width="1.3"><circle cx="7" cy="5" r="3.2"/><path d="M1 17v-1a6 6 0 0 1 12 0v1M12 2a3.2 3.2 0 0 1 0 6M15 11a6 6 0 0 1 2.5 5v1"/></svg>Social media</div>
    <div class="category"><svg viewBox="0 0 18 18" fill="none" stroke="#454a52" stroke-width="1.3"><path d="M1 2h3l2 10h9l2-7H5"/><circle cx="7" cy="15.5" r="1"/><circle cx="14" cy="15.5" r="1"/></svg>Shopping</div>
    <div class="category"><svg viewBox="0 0 18 18" fill="none" stroke="#454a52" stroke-width="1.3"><rect x="1.5" y="5" width="15" height="11"/><path d="M6 5V2.5h6V5M5 5v11M13 5v11"/></svg>Travel</div>
    <div class="category"><svg viewBox="0 0 18 18" fill="none" stroke="#454a52" stroke-width="1.3"><path d="M15.5 9A6.5 6.5 0 0 1 3.5 12.5M2.5 9A6.5 6.5 0 0 1 14.5 5.5M14.5 2v3.5H11M3.5 16v-3.5H7M10.5 7H8.2a1 1 0 0 0 0 2h1.6a1 1 0 0 1 0 2H7.5M9 6v1M9 11v1"/></svg>Banking</div>
    <div class="category"><svg viewBox="0 0 18 18" fill="none" stroke="#454a52" stroke-width="1.3"><rect x="1.5" y="3" width="15" height="12"/><path d="m1.5 3 7.5 7 7.5-7"/></svg>Emails</div>
    <div class="category"><svg viewBox="0 0 18 18" fill="none" stroke="#454a52" stroke-width="1.3"><path d="M1.5 3h5l1.5 2h8.5v10h-15z"/></svg>Test</div>
    <div class="category"><svg viewBox="0 0 18 18" fill="none" stroke="#454a52" stroke-width="1.3"><path d="M1.5 3h5l1.5 2h8.5v10h-15z"/></svg>Test</div>
    <div class="category"><svg viewBox="0 0 18 18" fill="none" stroke="#454a52" stroke-width="1.3"><path d="M1.5 3h5l1.5 2h8.5v10h-15z"/></svg>Test</div>
  </nav>

  <h2 class="section-title" style="left:442px;top:107px">Last Used</h2>
  <section class="recent">
    <div class="recent-col" style="left:42px;width:188px">
      <div class="entry"><svg viewBox="0 0 18 17" fill="none" stroke="#555" stroke-width="1.2"><rect x=".6" y=".6" width="16.8" height="15.8" rx="1.5"/><path d="M.6 4.5h16.8"/></svg>Test 3333</div>
      <div class="entry"><svg viewBox="0 0 18 17" fill="none" stroke="#555" stroke-width="1.2"><rect x=".6" y=".6" width="16.8" height="15.8" rx="1.5"/><path d="M.6 4.5h16.8"/></svg>Test 3333</div>
      <div class="entry"><svg viewBox="0 0 18 17" fill="none" stroke="#555" stroke-width="1.2"><rect x=".6" y=".6" width="16.8" height="15.8" rx="1.5"/><path d="M.6 4.5h16.8"/></svg>Test 3333</div>
      <div class="entry"><svg viewBox="0 0 18 17" fill="none" stroke="#555" stroke-width="1.2"><rect x=".6" y=".6" width="16.8" height="15.8" rx="1.5"/><path d="M.6 4.5h16.8"/></svg>Test 3333</div>
      <div class="entry"><svg viewBox="0 0 18 17" fill="none" stroke="#555" stroke-width="1.2"><rect x=".6" y=".6" width="16.8" height="15.8" rx="1.5"/><path d="M.6 4.5h16.8"/></svg>Test 3333</div>
      <div class="entry"><svg viewBox="0 0 18 17" fill="none" stroke="#555" stroke-width="1.2"><rect x=".6" y=".6" width="16.8" height="15.8" rx="1.5"/><path d="M.6 4.5h16.8"/></svg>Test 3333</div>
      <div class="entry"><svg viewBox="0 0 18 17" fill="none" stroke="#555" stroke-width="1.2"><rect x=".6" y=".6" width="16.8" height="15.8" rx="1.5"/><path d="M.6 4.5h16.8"/></svg>Test 3333</div>
    </div>
    <div class="recent-col" style="left:230px;width:230px;padding-left:42px">
      <div class="entry"><svg viewBox="0 0 18 17" fill="none" stroke="#555" stroke-width="1.2"><rect x=".6" y=".6" width="16.8" height="15.8" rx="1.5"/><path d="M.6 4.5h16.8"/></svg>Test 3333</div>
      <div class="entry"><svg viewBox="0 0 18 17" fill="none" stroke="#555" stroke-width="1.2"><rect x=".6" y=".6" width="16.8" height="15.8" rx="1.5"/><path d="M.6 4.5h16.8"/></svg>Test 3333</div>
      <div class="entry"><svg viewBox="0 0 18 17" fill="none" stroke="#555" stroke-width="1.2"><rect x=".6" y=".6" width="16.8" height="15.8" rx="1.5"/><path d="M.6 4.5h16.8"/></svg>Test 3333</div>
      <div class="entry"><svg viewBox="0 0 18 17" fill="none" stroke="#555" stroke-width="1.2"><rect x=".6" y=".6" width="16.8" height="15.8" rx="1.5"/><path d="M.6 4.5h16.8"/></svg>Test 3333</div>
      <div class="entry"><svg viewBox="0 0 18 17" fill="none" stroke="#555" stroke-width="1.2"><rect x=".6" y=".6" width="16.8" height="15.8" rx="1.5"/><path d="M.6 4.5h16.8"/></svg>Test 3333</div>
      <div class="entry"><svg viewBox="0 0 18 17" fill="none" stroke="#555" stroke-width="1.2"><rect x=".6" y=".6" width="16.8" height="15.8" rx="1.5"/><path d="M.6 4.5h16.8"/></svg>Test 3333</div>
      <div class="entry"><svg viewBox="0 0 18 17" fill="none" stroke="#555" stroke-width="1.2"><rect x=".6" y=".6" width="16.8" height="15.8" rx="1.5"/><path d="M.6 4.5h16.8"/></svg>Test 3333</div>
    </div>
    <div class="recent-col" style="left:460px;width:230px;padding-left:42px">
      <div class="entry"><svg viewBox="0 0 18 17" fill="none" stroke="#555" stroke-width="1.2"><rect x=".6" y=".6" width="16.8" height="15.8" rx="1.5"/><path d="M.6 4.5h16.8"/></svg>Test 3333</div>
      <div class="entry"><svg viewBox="0 0 18 17" fill="none" stroke="#555" stroke-width="1.2"><rect x=".6" y=".6" width="16.8" height="15.8" rx="1.5"/><path d="M.6 4.5h16.8"/></svg>Test 3333</div>
      <div class="entry"><svg viewBox="0 0 18 17" fill="none" stroke="#555" stroke-width="1.2"><rect x=".6" y=".6" width="16.8" height="15.8" rx="1.5"/><path d="M.6 4.5h16.8"/></svg>Test 3333</div>
      <div class="entry"><svg viewBox="0 0 18 17" fill="none" stroke="#555" stroke-width="1.2"><rect x=".6" y=".6" width="16.8" height="15.8" rx="1.5"/><path d="M.6 4.5h16.8"/></svg>Test 3333</div>
      <div class="entry"><svg viewBox="0 0 18 17" fill="none" stroke="#555" stroke-width="1.2"><rect x=".6" y=".6" width="16.8" height="15.8" rx="1.5"/><path d="M.6 4.5h16.8"/></svg>Test 3333</div>
      <div class="entry"><svg viewBox="0 0 18 17" fill="none" stroke="#555" stroke-width="1.2"><rect x=".6" y=".6" width="16.8" height="15.8" rx="1.5"/><path d="M.6 4.5h16.8"/></svg>Test 3333</div>
      <div class="entry"><svg viewBox="0 0 18 17" fill="none" stroke="#555" stroke-width="1.2"><rect x=".6" y=".6" width="16.8" height="15.8" rx="1.5"/><path d="M.6 4.5h16.8"/></svg>Test 3333</div>
    </div>
  </section>
</body>
</html>
```